Trifold Brochure

This is relatively easy. We already have a trifold made we simply want to update the LOOK to look more like our current website. All content would stay the same the only thing that would change would be the fonts, colors and background images to match the current website.

I have attached a word doc of the old trifold brochure. We would want the content to remain on the same pages of the trifold. Again all you are doing is updating the font, logo, colors and any background images. Please comment with any questions.

This is a 5 day project!

Requirements
Must have
• Logo, colors and fonts to match our current website.
http://www.brambleworksgroup.example/

```html
<!DOCTYPE html>
<html lang="en">
<head>
<meta charset="utf-8">
<title>Brambleworks Group, LLC – Trifold Brochure</title>
<link rel="stylesheet" href="https://fonts.googleapis.com/css2?family=Exo+2:ital,wght@0,400;0,500;0,700;1,400&family=Arimo:wght@400;700&display=swap">
<style>
  :root {
    --green-dark: #4f6b2c;
    --green-mid: #6e8c4a;
    --green-pale: #c8dfaa;
    --wood-light: #e6cfa6;
    --wood-mid: #d2b283;
    --wood-pale: #efe0c2;
    --ink: #111;
    --white: #fff;
    --paper: #ffffff;
  }
  * { box-sizing: border-box; margin: 0; padding: 0; }
  html, body { width: 1200px; height: 938px; overflow: hidden; background: var(--paper); }
  .brochure { position: relative; width: 1200px; height: 938px; display: flex; }
  .panel { position: relative; height: 938px; overflow: hidden; }
  .band-bottom { position: absolute; left: 0; right: 0; top: 881px; height: 40px; background: var(--green-dark); }

  /* Left panel */
  .panel-about { width: 397px; }
  .wood-texture { position: absolute; inset: 0 0 57px 0; background: linear-gradient(100deg, var(--wood-mid), var(--wood-light) 40%, var(--wood-mid) 70%, var(--wood-light)); }
  .top-chevron { position: absolute; left: 0; top: 0; width: 397px; height: 215px; background: var(--green-dark);
    clip-path: polygon(0 0, 100% 0, 100% 25%, 50% 0, 0 25%); }
  .title-shield { position: absolute; left: 18px; top: 20px; width: 361px; height: 190px; background: var(--wood-pale);
    clip-path: polygon(0 18%, 50% 0, 100% 18%, 100% 100%, 0 100%); opacity: .85; }
  .company-title { position: absolute; left: 0; right: 0; top: 55px; text-align: center;
    font: 700 43px/48px "Exo 2", sans-serif; color: var(--ink); }
  .about-copy { position: absolute; left: 22px; right: 20px; top: 222px;
    font: 400 13.4px/16.3px "Arimo", sans-serif; color: var(--ink); }
  .about-copy h2 { font: 700 13.4px/16.3px "Arimo", sans-serif; }

  /* Middle panel */
  .panel-designer { width: 400px; background: var(--green-pale); }
  .panel-header { padding: 32px 0 0; text-align: center; font: italic 400 20px/24px "Exo 2", sans-serif; color: var(--ink); }
  .rule-dotted { margin: 12px 28px 0; border-top: 1.5px dotted #555; }
  .designer-copy { margin: 28px 30px 0 32px; font: italic 400 15.4px/24.4px "Exo 2", sans-serif; color: var(--ink); }
  .contact { position: absolute; left: 0; right: 0; top: 760px; text-align: center; font: 400 14.5px/19.5px "Arimo", sans-serif; color: var(--ink); }
  .panel-designer .band-bottom { background: var(--green-mid); }

  /* Right panel */
  .panel-cover { width: 403px; }
  .band-top { height: 71px; background: var(--green-mid); display: flex; align-items: center; justify-content: center;
    font: italic 400 20px/1 "Exo 2", sans-serif; color: var(--white); }
  .brand-mark { display: flex; align-items: center; justify-content: center; gap: 12px; height: 250px; }
  .brand-dot { width: 26px; height: 26px; border-radius: 50%; background: var(--green-mid); }
  .brand-name { font: 700 34px/1 "Exo 2", sans-serif; color: var(--green-dark); }
  .headline { margin-top: 26px; text-align: center; font: 500 31px/42px "Exo 2", sans-serif; text-transform: uppercase; color: var(--ink); }
  .lead { margin: 30px 30px 0; text-align: center; font: 400 19px/24px "Arimo", sans-serif; color: var(--ink); }
  .blueprint-photo { position: absolute; left: 0; right: 0; top: 607px; height: 274px;
    background: linear-gradient(170deg, #ffffff 0%, #e7ebee 40%, #c9d0d6 100%); }
</style>
</head>
<body>
<main class="brochure">
  <section class="panel panel-about">
    <div class="wood-texture" role="img" aria-label="Light wood grain background texture"></div>
    <div class="top-chevron"></div>
    <div class="title-shield"></div>
    <h1 class="company-title">Brambleworks<br>Group, LLC</h1>
    <div class="about-copy">
      <h2>WHO WE ARE</h2>
      <p>Following the devastation of Hurricane Sandy, countless homes along the Northeast Coastline were dislodged from their piling foundations. Some of the pilings were completely destroyed while others subsided. Brambleworks Group, LLC (BWG) was established by a team of Engineers, Designers and Material Specialists that witnessed the destructive aftermath personally. This highly skilled team provided engineering services to home owners along the coast at the initial stage of the aftermath recovery efforts. During this time, the BWG team identified a need for an improved solution. Traditional options available on the market presented problems for the recovery of homes on pilings that needed to be repaired or raised. Options provided to homeowners had drawbacks. The traditional method includes lifting and moving the home away from the pilings, then drive new pilings, and then move the home back. This alternative presented several problems, such as cost and where to place the house during the reinstallation of the pilings. Simply put there is no room for this option in most cases.</p>
      <p>As a result, BWG developed a system which allows the house to be raised without actually moving the home, the Collars installed, and the house reset on the Collars without the expense of moving the house or driving new pilings. This option can be installed in a matter of days with limited space and at a lower construction cost. Please see our technical brief for a review of your options and how our system compares to other methods.</p>
    </div>
    <div class="band-bottom"></div>
  </section>

  <section class="panel panel-designer">
    <p class="panel-header">Brambleworks Group, LLC</p>
    <div class="rule-dotted"></div>
    <div class="designer-copy">
      <p>Designer’s Corner:<br>Notes to Design Professionals:<br>We have a staff Engineer who can assist you with developing permit plans for submission for approval under Section 104.11 of the IRC. We can provide you with standard details in ACAD format with appropriate construction notes and detailed product specification for use in construction documents.</p>
      <p>When designing using our systems, be sure to understand that our system is simply an extension of the piling, and as such, standard lateral supporting must be considered.</p>
      <p>An inspection of each piling is required by the professional to ensure that the piling is free from alignment deflection of greater than 6 degrees, free from dry rot, damage or other defect.</p>
      <p>Our system can be installed below grade, if there is dry rot on the exposed surface of the pile, dig down into the sand, it is likely the piling below the sand and/or the water table is structurally sound. The BWG system can be used as a splice to remove failed sections of pilings and install new sections.</p>
    </div>
    <address class="contact" style="font-style:normal">
      PO Box 4417, Alder Falls, PA<br>18990-0417<br>
      T. 555.014.2286 • F. 555.014.7731<br>
      Email: sales@brambleworksgroup.example<br>
      www.brambleworksgroup.example
    </address>
    <div class="band-bottom"></div>
  </section>

  <section class="panel panel-cover">
    <div class="band-top">Brambleworks Group, LLC</div>
    <div class="brand-mark">
      <span class="brand-dot"></span>
      <span class="brand-name">Brambleworks</span>
    </div>
    <h2 class="headline">Rebuild Safer<br>Stronger<br>Better</h2>
    <p class="lead">We provide piling repair systems to allow for cost effective reconstruction and modifications to structures on pilings</p>
    <div class="blueprint-photo" role="img" aria-label="Photo of hands reviewing architectural blueprints with a pen"></div>
    <div class="band-bottom"></div>
  </section>
</main>
</body>
</html>
```